Business card for different employees

A professional new updated design incorporating our current business's color themes and styles such as our on-site service trucks decals included in pictures attached. Our current business card is very simple and not professionally designed. We are a small family business but want a professional corporate look.

Target Market(s)

Cards to be handed out to new customers , corperate meetings. For our on site service operators.

Industry/Entity Type

Hydraulic

Contact Information for Business Card

Address, website, phone number, email, logo.
slogan - "Industry chosen hose and fittings provider".
24/7 on-site service , supply and hose management
Experienced , indpendant , family owned

Font styles to use
Sans Serif

Requirements
Must have
• Easily editable so that I can add different names and different roles for employees etc.
Nice to have
• Freedom with colour doesn't necessarily have to be blue but that is our company colour theme with trucks and logo so makes sense for the card to have blue like the trucks.

```html
<!DOCTYPE html>
<html lang="en">
<head>
<meta charset="UTF-8">
<title>Meridian Hose and Fittings – Business Card</title>
<link href="https://fonts.googleapis.com/css2?family=Krona+One&family=League+Spartan:wght@400;500;700&display=swap" rel="stylesheet">
<style>
  :root {
    --stage: #2a2a2c;
    --brand-blue: #2f46a6;
    --brand-blue-deep: #26398a;
    --card-black: #1b1b1d;
    --white: #ffffff;
    --soft-white: #e9ecf6;
  }
  * { box-sizing: border-box; margin: 0; padding: 0; }
  html, body {
    width: 1200px; height: 900px; overflow: hidden;
    background: var(--stage);
  }
  .stage { position: relative; width: 1200px; height: 900px; }
  .card {
    position: absolute; left: 250px; width: 700px; height: 400px;
    overflow: hidden;
    box-shadow: 0 12px 30px rgba(0,0,0,0.45);
  }
  .card--front { top: 35px; background: var(--brand-blue); }
  .card--back  { top: 465px; background: var(--card-black); }

  /* Brand lockup */
  .brand { position: absolute; display: flex; align-items: center; gap: 18px; }
  .brand__dot {
    width: 70px; height: 70px; border-radius: 50%;
    background: var(--white); flex: none;
  }
  .brand__name {
    font-family: "Krona One", sans-serif;
    color: var(--white); line-height: 1.25; white-space: nowrap;
  }
  .brand__name-main { display: block; font-size: 40px; letter-spacing: 1px; }
  .brand__name-sub  { display: block; font-size: 15px; letter-spacing: 4px; }
  .card--front .brand { left: 40px; top: 40px; }

  /* Front content */
  .slogan {
    position: absolute; left: 40px; top: 158px;
    font-family: "Krona One", sans-serif; font-size: 15px;
    color: var(--white); letter-spacing: 1px; text-transform: uppercase;
  }
  .service { position: absolute; left: 0; top: 205px; display: flex; align-items: center; gap: 22px; }
  .service__badge {
    background: var(--white); color: var(--brand-blue);
    font-family: "Krona One", sans-serif; font-size: 42px;
    padding: 6px 26px 6px 40px; line-height: 1.1;
  }
  .service__lines {
    font-family: "Krona One", sans-serif; font-size: 15px; color: var(--white);
    text-transform: uppercase; letter-spacing: 1px; line-height: 1.6;
  }
  .values {
    position: absolute; left: 40px; top: 300px;
    font-family: "Krona One", sans-serif; font-size: 17px; color: var(--white);
    text-transform: uppercase; letter-spacing: 1px;
  }

  /* Back content */
  .card--back .brand { left: 40px; top: 118px; gap: 14px; }
  .card--back .brand__dot { width: 60px; height: 60px; }
  .card--back .brand__name-main { font-size: 30px; }
  .card--back .brand__name-sub { font-size: 11px; letter-spacing: 3px; }

  .divider { position: absolute; left: 380px; width: 3px; background: var(--brand-blue); }
  .divider--top { top: 110px; height: 58px; }
  .divider--bottom { top: 182px; height: 92px; }

  .person { position: absolute; left: 400px; top: 108px; white-space: nowrap; }
  .person__name {
    font-family: "Krona One", sans-serif; font-size: 19px; line-height: 1.3;
    color: var(--brand-blue); letter-spacing: 1px; text-transform: uppercase;
  }
  .person__role {
    font-family: "League Spartan", sans-serif; font-size: 20px; color: var(--white);
    margin-top: 4px;
  }
  .contact {
    position: absolute; left: 400px; top: 184px; list-style: none; white-space: nowrap;
    font-family: "League Spartan", sans-serif; font-size: 19px; color: var(--white);
  }
  .contact__item { display: flex; align-items: center; gap: 12px; height: 30px; }
  .contact__icon { width: 20px; height: 20px; flex: none; }

  .address-band {
    position: absolute; left: 0; right: 0; bottom: 25px; height: 60px;
    background: var(--brand-blue);
    display: flex; align-items: center; justify-content: center;
    font-family: "League Spartan", sans-serif; font-size: 22px; color: var(--white);
  }
</style>
</head>
<body>
<main class="stage">

  <section class="card card--front" aria-label="Card front">
    <div class="brand">
      <span class="brand__dot"></span>
      <span class="brand__name">
        <span class="brand__name-main">MERIDIAN</span>
        <span class="brand__name-sub">HOSE AND FITTINGS</span>
      </span>
    </div>
    <p class="slogan">Industry chosen hose and fittings provider</p>
    <div class="service">
      <span class="service__badge">24/7</span>
      <p class="service__lines">On-site service<br>Supply and hose management</p>
    </div>
    <p class="values">Experienced · Indpendant · Family owned</p>
  </section>

  <section class="card card--back" aria-label="Card back">
    <div class="brand">
      <span class="brand__dot"></span>
      <span class="brand__name">
        <span class="brand__name-main">MERIDIAN</span>
        <span class="brand__name-sub">HOSE AND FITTINGS</span>
      </span>
    </div>

    <span class="divider divider--top"></span>
    <span class="divider divider--bottom"></span>

    <div class="person">
      <h1 class="person__name">Dale Harrower</h1>
      <p class="person__role">Owner/ CEO</p>
    </div>

    <ul class="contact">
      <li class="contact__item">
        <svg class="contact__icon" viewBox="0 0 24 24" fill="none" stroke="#2f46a6" stroke-width="2"><circle cx="12" cy="12" r="10"/><path d="M8 7c0 5 4 9 9 9l1-2-3-1-1 1c-2-1-3-2-4-4l1-1-1-3z" fill="#2f46a6" stroke="none"/></svg>
        <span>0400 123 456</span>
      </li>
      <li class="contact__item">
        <svg class="contact__icon" viewBox="0 0 24 24" fill="none" stroke="#2f46a6" stroke-width="2"><rect x="2" y="5" width="20" height="14"/><path d="M2 5l10 8 10-8"/></svg>
        <span>meridianhose@example.com</span>
      </li>
      <li class="contact__item">
        <svg class="contact__icon" viewBox="0 0 24 24" fill="none" stroke="#2f46a6" stroke-width="2"><circle cx="12" cy="12" r="10"/><path d="M2 12h20M12 2c3 3 3 17 0 20M12 2c-3 3-3 17 0 20"/></svg>
        <span>www.meridianhose.com.au</span>
      </li>
    </ul>

    <p class="address-band">48 Kestrel Rd. Suite 200. AU 3052</p>
  </section>

</main>
</body>
</html>
```